A billboard for Harlow Ridge Construction size 36.5’ x 14.5’

Hi guys. We are purchasing a billboard and are looking for a design (size 36.5’ x 14.5’). Our slogan is "Quality you deserve, service you can count on". The goal of this billboard is brand recognition primarily letting people know we do roofs. Attached are logos that can be used if needed. Not necessarily all of them need to be used.

Target Market(s)

Residents in the local areas needing or thinking about a roof replacement

Industry/Entity Type

Roofing

Requirements
Must have
• Logo and services (roof replacement, gutters, siding, and snow removal)
Nice to have
• take a look at our website for ideas www.harlowridgeconstruction.example

```html
<!DOCTYPE html>
<html lang="en">
<head>
<meta charset="utf-8">
<title>Harlow Ridge Construction Billboard</title>
<link href="https://fonts.googleapis.com/css2?family=Montserrat:wght@300;400;600;700&display=swap" rel="stylesheet">
<style>
  :root {
    --red: #ec0b0b;
    --white: #ffffff;
    --ink: #1c1c1c;
    --band: rgba(38, 36, 34, 0.86);
    --stage: #d6d6d6;
    --badge-blue: #0f5c86;
    --badge-grey: #b9b9b9;
  }
  * { box-sizing: border-box; margin: 0; padding: 0; }
  html, body { width: 934px; height: 1200px; overflow: hidden; }
  body {
    background: var(--stage);
    font-family: "Montserrat", sans-serif;
    position: relative;
  }
  .billboard {
    position: absolute;
    left: 37px; top: 429px;
    width: 860px; height: 342px;
    background: var(--white);
    box-shadow: 0 10px 22px rgba(0,0,0,0.35);
    overflow: hidden;
  }
  .brand-panel {
    position: absolute; left: 0; top: 0;
    width: 383px; height: 342px;
    background: var(--red);
  }
  .logo-tab {
    position: absolute; left: 47px; top: 0;
    width: 283px; height: 103px;
  }
  .logo-tab svg { position: absolute; inset: 0; }
  .logo-name {
    position: absolute; left: 0; right: 0; top: 24px;
    display: flex; align-items: center; justify-content: center; gap: 9px;
    color: var(--ink); font-weight: 600; font-size: 15px; line-height: 1.15;
  }
  .logo-name .mark { width: 14px; height: 14px; background: var(--red); flex: none; }
  .slogan {
    position: absolute; left: 45px; top: 118px;
    color: var(--white); line-height: 1;
  }
  .slogan span { display: block; font-size: 40px; letter-spacing: 0.2px; }
  .slogan .strong { font-weight: 700; }
  .slogan .light { font-weight: 400; }
  .slogan span + span { margin-top: 7px; }
  .house-photo {
    position: absolute; left: 383px; top: 0;
    width: 477px; height: 270px;
    background: linear-gradient(180deg, #8fb5e0 0%, #9fb9cc 18%, #7e7c74 38%, #8d7a6d 62%, #6f5f55 100%);
  }
  .services {
    position: absolute; left: 383px; top: 190px;
    width: 477px; height: 80px;
    background: var(--band);
    display: grid;
    grid-template-columns: 242px 1fr;
    grid-template-rows: 1fr 1fr;
    padding: 10px 0 8px 37px;
  }
  .service {
    display: flex; align-items: center; gap: 12px;
    color: var(--white); font-weight: 600; font-size: 15px;
  }
  .service-icon {
    width: 19px; height: 19px; background: var(--red); border-radius: 2px; flex: none;
  }
  .service-icon svg { display: block; }
  .contact-strip {
    position: absolute; left: 383px; top: 270px;
    width: 477px; height: 72px;
  }
  .phone {
    position: absolute; left: 39px; top: 13px;
    display: flex; align-items: center; gap: 6px;
    font-weight: 700; font-size: 21px; color: var(--ink);
  }
  .web {
    position: absolute; left: 39px; top: 43px;
    display: flex; align-items: center; gap: 7px;
    font-size: 9.5px; color: var(--ink);
  }
  .web b { color: var(--red); font-weight: 600; }
  .badge-primary {
    position: absolute; left: 257px; top: 20px;
    width: 90px; height: 33px; background: var(--badge-blue); border-radius: 2px;
  }
  .divider {
    position: absolute; top: 22px; width: 1px; height: 30px; background: #c9c9c9;
  }
  .badge-small {
    position: absolute; top: 24px; border-radius: 2px; background: var(--badge-grey);
  }
</style>
</head>
<body>
  <div class="billboard">
    <section class="brand-panel">
      <div class="logo-tab">
        <svg width="283" height="103" viewBox="0 0 283 103" aria-hidden="true">
          <polygon points="0,0 283,0 283,70 141,103 0,70" fill="#ffffff"/>
        </svg>
        <div class="logo-name">
          <span class="mark"></span>
          <span>Harlow Ridge<br>Construction</span>
        </div>
      </div>
      <h1 class="slogan">
        <span class="strong">Quality You</span>
        <span class="light">Deserve,</span>
        <span class="strong">Service You</span>
        <span class="light">Can Count On</span>
      </h1>
    </section>

    <div class="house-photo" role="img" aria-label="Photo of a two-storey brick house with a new grey shingle roof under a blue sky"></div>

    <ul class="services">
      <li class="service"><span class="service-icon"></span>Roof Replacement</li>
      <li class="service"><span class="service-icon"></span>Siding</li>
      <li class="service"><span class="service-icon"></span>Gutters</li>
      <li class="service"><span class="service-icon"></span>Snow Removal</li>
    </ul>

    <div class="contact-strip">
      <div class="phone">
        <svg width="15" height="15" viewBox="0 0 24 24" aria-hidden="true"><path d="M6.6 10.8a15.1 15.1 0 0 0 6.6 6.6l2.2-2.2a1 1 0 0 1 1-.25 11.4 11.4 0 0 0 3.6.57 1 1 0 0 1 1 1V20a1 1 0 0 1-1 1A17 17 0 0 1 3 4a1 1 0 0 1 1-1h3.5a1 1 0 0 1 1 1c0 1.25.2 2.45.57 3.6a1 1 0 0 1-.25 1z" fill="#1c1c1c"/></svg>
        262-555-0148
      </div>
      <div class="web">
        <svg width="12" height="12" viewBox="0 0 24 24" aria-hidden="true"><g fill="none" stroke="#ec0b0b" stroke-width="2"><circle cx="12" cy="12" r="10"/><ellipse cx="12" cy="12" rx="4.5" ry="10"/><line x1="2" y1="12" x2="22" y2="12"/><line x1="4" y1="7" x2="20" y2="7"/><line x1="4" y1="17" x2="20" y2="17"/></g></svg>
        <span>www.<b>harlowridgeconstruction</b>.example</span>
      </div>
      <div class="badge-primary"></div>
      <div class="divider" style="left:357px"></div>
      <div class="badge-small" style="left:370px;width:26px;height:26px"></div>
      <div class="divider" style="left:405px"></div>
      <div class="badge-small" style="left:416px;width:40px;height:26px"></div>
    </div>
  </div>
</body>
</html>
```